Plindy Orchards Business Card Design

My company is about Natural products made from Bees Wax, of which I am farming/raising. Products like Honey when in season, body butter, hand cream, lotions, lip balm, soap and more! All Natural, with Beeswax as the base, as it has large healing properties for moisturizing and nourishing your skin.
I would prefer lots of yellows, browns, and blacks (but am open)! I think black ink on the artwork may show up the best. But your the professionals!
The artwork is very dear to me, as my son, Warren did this in the hospital when he was diagnosed with Leukemia, of which he did not survive, at eighteen.
Is it possible to put his initials on this? WDT in light colored ink.
NO BEES, NO US! Oops! I need my name on there. Paula Vantreck and number 210-555-0147. Thank you all so much.

Hospital

Plindy Orchards
All Natural Products
Paula Vantreck
210-555-0147
PlindyOrchards@mailbrook.example

```html
<!DOCTYPE html>
<html lang="en">
<head>
<meta charset="utf-8">
<title>Plindy Orchards Business Card</title>
<link rel="stylesheet" href="https://fonts.googleapis.com/css2?family=Cinzel:wght@400;500&family=Lato:wght@300;400;700&display=swap">
<style>
  :root {
    --page-bg: #e9e4dc;
    --card-black: #0d0d0d;
    --card-black-edge: #1c1c1c;
    --gold: #cdb93a;
    --white: #f2f2f2;
    --art-red: #d9474f;
    --art-orange: #ef8a2a;
    --art-yellow: #f1cf2e;
    --art-green: #5f9a4c;
    --art-blue: #6a9bc0;
    --art-pink: #e77a8c;
    --art-purple: #6b4a8e;
  }
  * { margin: 0; padding: 0; box-sizing: border-box; }
  html, body {
    width: 1200px;
    height: 1000px;
    overflow: hidden;
    background: var(--page-bg);
  }
  .canvas {
    position: relative;
    width: 1200px;
    height: 1000px;
  }
  .card {
    position: absolute;
    left: 250px;
    width: 700px;
    height: 400px;
    border-radius: 4px;
    box-shadow: 0 10px 28px rgba(0,0,0,0.28);
    overflow: hidden;
  }
  .card-front {
    top: 70px;
    background:
      radial-gradient(circle at 22% 30%, var(--art-purple) 0, transparent 22%),
      radial-gradient(circle at 50% 12%, var(--art-orange) 0, transparent 30%),
      radial-gradient(circle at 80% 18%, var(--art-yellow) 0, transparent 28%),
      radial-gradient(circle at 88% 65%, var(--art-blue) 0, transparent 38%),
      radial-gradient(circle at 15% 75%, var(--art-pink) 0, transparent 35%),
      radial-gradient(circle at 45% 85%, var(--art-red) 0, transparent 35%),
      radial-gradient(circle at 30% 50%, var(--art-green) 0, transparent 25%),
      linear-gradient(135deg, var(--art-red), var(--art-orange) 40%, var(--art-blue));
  }
  .card-back {
    top: 530px;
    background: radial-gradient(ellipse at 50% 40%, var(--card-black-edge), var(--card-black) 75%);
    text-align: center;
    color: var(--white);
    padding-top: 52px;
  }
  .brand-name {
    font-family: "Cinzel", serif;
    font-weight: 400;
    font-size: 42px;
    letter-spacing: 2px;
    color: var(--gold);
    line-height: 1;
  }
  .brand-subtitle {
    font-family: "Lato", sans-serif;
    font-weight: 300;
    font-size: 25px;
    letter-spacing: 4px;
    margin-top: 8px;
    line-height: 1.1;
  }
  .tagline {
    font-family: "Lato", sans-serif;
    font-weight: 300;
    font-size: 18px;
    letter-spacing: 2.5px;
    color: var(--gold);
    margin-top: 6px;
  }
  .tagline .initials {
    color: var(--white);
    font-weight: 700;
  }
  .person-name {
    font-family: "Cinzel", serif;
    font-size: 26px;
    color: var(--gold);
    margin-top: 40px;
    letter-spacing: 1px;
  }
  .contact {
    font-family: "Lato", sans-serif;
    font-size: 18px;
    margin-top: 22px;
    line-height: 1.65;
  }
  .contact .label {
    color: var(--gold);
    font-weight: 700;
  }
  .product-list {
    font-family: "Lato", sans-serif;
    font-size: 18px;
    color: var(--gold);
    letter-spacing: 0.5px;
    margin-top: 24px;
  }
</style>
</head>
<body>
  <main class="canvas">
    <section class="card card-front" role="img" aria-label="Colourful hand-painted artwork with swirling red, orange, yellow, green, blue and pink shapes radiating from a central star"></section>

    <section class="card card-back">
      <h1 class="brand-name">Plindy Orchards</h1>
      <p class="brand-subtitle">ALL NATURAL PRODUCTS</p>
      <p class="tagline"><span class="initials">WDT</span>.NO BEES, NO US! OOPS!</p>
      <p class="person-name">Paula Vantreck</p>
      <div class="contact">
        <p><span class="label">P:</span> 210-555-0147</p>
        <p><span class="label">E:</span> PlindyOrchards@mailbrook.example</p>
      </div>
      <p class="product-list">Body Butter, Lotion, Hand Cream, Lip Balm, Soap and More!</p>
    </section>
  </main>
</body>
</html>
```